RW Business Card Design

My company provides advising/training and coaching services to business owners who want better financial results and better work/life balance. We help them through creating custom plans supported with education, strategic thinking and accountability.

We also help through some online courses which are geared to smaller businesses.
Updates

please also include our nth american contact # +1 555 208 4471

Industry/Entity Type

Financial

Contact Information for Business Card

Morgan Halberd
morgan@morganhalberd-example.com
+61 400 555 917
www.morganhalberd-example.com

```html
<!DOCTYPE html>
<html lang="en">
<head>
<meta charset="utf-8">
<title>Morgan Halberd Business Card</title>
<link rel="stylesheet" href="https://fonts.googleapis.com/css2?family=Questrial&family=Arimo:wght@400&display=swap">
<style>
  :root {
    --stage: #000000;
    --label: #ffffff;
    --card: #dcddde;
    --brand-blue: #1f74bb;
    --ink: #1e1e1e;
  }
  * { margin: 0; padding: 0; box-sizing: border-box; }
  html, body {
    width: 1200px;
    height: 1200px;
    overflow: hidden;
    background: var(--stage);
  }
  .sheet {
    position: relative;
    width: 1200px;
    height: 1200px;
  }
  .side-label {
    position: absolute;
    left: 280px;
    font-family: "Questrial", sans-serif;
    font-size: 34px;
    color: var(--label);
    line-height: 1;
  }
  .side-label--front { top: 110px; }
  .side-label--back { top: 590px; }

  .card {
    position: absolute;
    left: 280px;
    width: 637px;
    height: 393px;
    background: var(--card);
    overflow: hidden;
  }
  .card--front { top: 157px; }
  .card--back { top: 636px; }

  .brand {
    position: absolute;
    left: 60px;
    top: 52px;
    display: flex;
    align-items: center;
    gap: 18px;
  }
  .brand-dot {
    width: 46px;
    height: 46px;
    border-radius: 50%;
    background: var(--brand-blue);
  }
  .brand-name {
    font-family: "Questrial", sans-serif;
    font-size: 46px;
    letter-spacing: 0.5px;
    color: var(--brand-blue);
    line-height: 1;
  }

  .formula {
    position: absolute;
    left: 0;
    right: 0;
    top: 162px;
    text-align: center;
    font-family: "Questrial", sans-serif;
    color: var(--brand-blue);
  }
  .formula-line {
    font-size: 17px;
    line-height: 20.5px;
  }
  .formula-result {
    margin-top: 12px;
    font-size: 46px;
    line-height: 1;
  }

  .contact {
    position: absolute;
    right: 32px;
    top: 176px;
    text-align: right;
    font-family: "Arimo", sans-serif;
    font-size: 14px;
    line-height: 17px;
    color: var(--ink);
  }
  .contact-block + .contact-block { margin-top: 17px; }
</style>
</head>
<body>
<div class="sheet">
  <div class="side-label side-label--front">Front</div>
  <section class="card card--front">
    <div class="brand">
      <span class="brand-dot"></span>
      <span class="brand-name">MORGANHALBERD</span>
    </div>
    <div class="formula">
      <p class="formula-line">Knowledge</p>
      <p class="formula-line">+</p>
      <p class="formula-line">Planning</p>
      <p class="formula-line">x</p>
      <p class="formula-line">Action</p>
      <p class="formula-line">=</p>
      <p class="formula-result">Success</p>
    </div>
  </section>

  <div class="side-label side-label--back">Back</div>
  <section class="card card--back">
    <div class="contact">
      <p class="contact-block">Morgan Halberd</p>
      <p class="contact-block">morgan@morganhalberd-example.com</p>
      <div class="contact-block">
        <p>Australian Office: +61 400 555 917</p>
        <p>North American Office: +1 555 208 4471</p>
      </div>
      <p class="contact-block">www.morganhalberd-example.com</p>
    </div>
  </section>
</div>
</body>
</html>
```